Wedding Photo Studio needs custom webpage

I'm changing up my service offering to offer multiple editing styles. I'm looking to update my website to reflect that but still showcase my dreamy edits as an attention grabbing part of the website.

I will have 4 color editing styles (Colm's Hallmark, Bright & Airy, Silken Oak, Dreamy) and one black and white style. I have attached sample images in each style.

I also attached a couple dreamy edits that can be used as attention grabbing images.

I'm hoping for some functionality that perhaps takes a single image and divides it by 4 to show 25% in each style that can be clicked on and would 'maximize' the carousel to that style but still have a functionality to go to a different style after being maximized.

You can see www.colmvphotography.com for the current design and content. It doesn't have to be too different (but can be). It just needs to showcase the multiple editing styles effectively.

Target Market(s)

Couples who are having $20-50k weddings.

Industry/Entity Type

Photography

Coding

Coded - Design and coding required

Number of Pages Required

3 page

Colors

Designer to choose colors to be used in the design.

Requirements
Must have
• Pricing page with toggles for (off-season/on-season, Saturday/non-saturday) accurate pricing, good way to show multiple editing style photos.

```html
<!DOCTYPE html>
<html lang="en">
<head>
<meta charset="utf-8">
<title>Colm V Photography</title>
<link href="https://fonts.googleapis.com/css2?family=Poppins:ital,wght@0,300;0,400;0,500;1,300&family=Allura&display=swap" rel="stylesheet">
<style>
:root{
  --ink:#2f2f33;
  --body:#5c5c60;
  --accent:#1d5ea8;
  --teal:#7fb0c4;
  --cream:#f7f2ec;
  --panel:#fbfbfa;
  --footer:#2a2a2c;
  --white:#ffffff;
}
*{box-sizing:border-box;margin:0;padding:0}
html,body{width:1200px;height:4006px;overflow:hidden}
body{position:relative;font-family:'Poppins',sans-serif;color:var(--ink);
  background:linear-gradient(180deg,#f6efe7 0%,#f4eee6 20%,#efe9dc 33%,#f2f0df 36%,#f3f5f6 48%,#f4f7f8 62%,#eef1ea 70%,#f3f3f1 80%,#f6f6f6 92%)}
.abs{position:absolute}
.script{font-family:'Allura',cursive;font-weight:400}
.caps{text-transform:uppercase;font-weight:400;letter-spacing:0}

/* header */
.site-header{left:0;top:0;width:1200px;height:104px;background:var(--white)}
.brand{left:47px;top:28px;display:flex;align-items:center;gap:12px;color:var(--accent);font-family:'Poppins',sans-serif;font-weight:400;font-size:24px;letter-spacing:.5px;white-space:nowrap}
.brand .ring{width:40px;height:40px;border:2px solid var(--accent);border-radius:50%;flex:none}
.main-nav{top:44px;left:0;height:20px}
.main-nav a{position:absolute;font-size:16px;color:#3a3a3e;text-decoration:none;white-space:nowrap;text-transform:uppercase}
.main-nav a.active{color:var(--accent)}

/* hero */
.hero{left:0;top:104px;width:1200px;height:598px;
  background:linear-gradient(100deg,#d7b89a 0%,#e6c5a6 25%,#cfb49d 45%,#a8a5a8 65%,#8c8a90 85%,#b6aaa4 100%)}
.hero-title{left:112px;top:315px;color:var(--white)}
.hero-title .script{font-size:70px;line-height:1;display:block}
.hero-title .caps{font-size:58px;line-height:1;display:block;margin-top:18px;font-weight:500}
.round-btn{width:52px;height:52px;border-radius:50%;background:var(--white);box-shadow:0 2px 8px rgba(0,0,0,.15);display:flex;align-items:center;justify-content:center}

/* about */
.photo{background:linear-gradient(180deg,#e9a84c,#d8b06a 60%,#9aa04e)}
.photo.sea{background:linear-gradient(180deg,#4f8bd0,#7fb4e6 55%,#5a6e7e)}
.section-script{font-size:50px;color:var(--ink);line-height:1}
.section-title{font-size:38px;color:var(--ink);line-height:52px;font-weight:400}
.about-copy{left:637px;top:1002px;width:460px;font-size:16px;line-height:28.5px;color:var(--body);font-weight:300}
.outline-btn{border:1px solid #3a3a3e;background:transparent;font-family:'Poppins',sans-serif;font-size:17px;color:var(--ink);display:flex;align-items:center;justify-content:center;text-transform:uppercase}

/* portfolio */
.centered{left:0;width:1200px;text-align:center}
.portfolio-panel{left:73px;top:1632px;width:1054px;height:439px;background:var(--panel)}
.style-card{top:1684px;width:221px}
.style-card .frame{height:290px;background:linear-gradient(180deg,#8a6a55,#b44d3e 35%,#d8d2cc 70%,#6f6356)}
.style-card .frame.airy{background:linear-gradient(180deg,#b69d8c,#dd7d73 35%,#f1ece8 70%,#a89e90)}
.style-card .frame.oak{background:linear-gradient(180deg,#6e5443,#9a4c36 35%,#d5c8b8 70%,#5e4c3a)}
.style-card .frame.mono{background:linear-gradient(180deg,#555,#8a8a8a 35%,#dcdcdc 70%,#4e4e4e)}
.style-card p{text-align:center;font-size:19px;margin-top:20px;color:var(--ink)}

/* testimonials */
.review{background:var(--white);text-align:center;padding:0 26px}
.review q{display:block;font-style:italic;font-weight:300;font-size:16.5px;line-height:26px;color:var(--body);quotes:none}
.review .who{font-size:19px;margin-top:22px;color:var(--ink)}
.review.featured{background:var(--teal)}
.review.featured q,.review.featured .who{color:var(--white)}
.avatar{width:90px;height:90px;border-radius:50%;background:radial-gradient(circle,#f3c8a6,#c88766 70%,#8a5a44)}
.avatar.blue{background:radial-gradient(circle,#ffffff,#c8d7e8 70%,#8fa7c4)}
.dots{top:2831px;left:555px;display:flex;gap:6px}
.dots span{width:11px;height:11px;border:1px solid #6d8ea0;border-radius:50%}
.dots span.on{background:var(--teal);border-color:var(--teal)}

/* contact */
.field{background:var(--white);font-size:16px;color:#6a6a6e;padding:16px 16px;font-weight:400}

/* footer */
.site-footer{left:0;top:3722px;width:1200px;height:284px;background:var(--footer);color:var(--white)}
.footer-brand{left:40px;top:60px;display:flex;align-items:center;gap:14px;font-size:27px;letter-spacing:.5px;white-space:nowrap;font-weight:400}
.footer-brand .ring{width:50px;height:50px;border:2px solid var(--white);border-radius:50%;flex:none}
.footer-text{left:486px;top:70px;font-size:17px;line-height:28px;font-weight:500;width:430px}
.contact-line{left:490px;font-size:16px;display:flex;align-items:center;gap:8px;font-weight:300;white-space:nowrap}
.social{width:46px;height:46px;border:1.5px solid var(--white);border-radius:50%}
.copyright{left:110px;top:195px;font-size:16px;font-weight:300;white-space:nowrap}
</style>
</head>
<body>

<header class="abs site-header">
  <div class="abs brand"><span class="ring"></span>Colm V Photography</div>
  <nav class="abs main-nav">
    <a class="active" style="left:463px">Home</a>
    <a style="left:553px">About</a>
    <a style="left:651px">Portfolio</a>
    <a style="left:783px">Blog</a>
    <a style="left:867px">Pricing</a>
    <a style="left:976px">Contact Me</a>
  </nav>
</header>

<section class="abs hero" role="img" aria-label="Couple sharing a kiss on a bridge balcony above a river at sunset"></section>
<div class="abs hero-title">
  <span class="script">Colm Varga</span>
  <span class="caps">Photography</span>
</div>
<div class="abs round-btn" style="left:543px;top:676px"><svg width="16" height="16" viewBox="0 0 16 16"><path d="M10 3 5 8l5 5" fill="none" stroke="#333" stroke-width="1.8"/></svg></div>
<div class="abs round-btn" style="left:605px;top:676px"><svg width="16" height="16" viewBox="0 0 16 16"><path d="M6 3l5 5-5 5" fill="none" stroke="#333" stroke-width="1.8"/></svg></div>

<!-- about -->
<div class="abs photo" style="left:95px;top:883px;width:225px;height:307px" role="img" aria-label="Couple embracing in a golden meadow at sunset"></div>
<div class="abs photo sea" style="left:339px;top:813px;width:227px;height:307px" role="img" aria-label="Couple kissing on a pier by the lake"></div>
<div class="abs script" style="left:362px;top:1150px;font-size:46px;color:var(--ink)">Colm Varga</div>

<div class="abs script section-script" style="left:643px;top:805px">About Us</div>
<h2 class="abs section-title caps" style="left:637px;top:874px">Welcome to<br>Colm-V Photography</h2>
<p class="abs about-copy">I am an accountant by day, photographer by night. I once read a happy life is had by loving your job, loving your creative hobby and the love of family; photography is one part of that for me. I focus primarily on wedding photography in southern Ontario. I cover Toronto, Hamilton, Kitchener, Waterloo, London and anywhere in the world you want to send me. If you like what I do, please reach out; I'm happy to meet with you and chat more about your big day.</p>
<div class="abs outline-btn" style="left:637px;top:1294px;width:148px;height:56px">Read More</div>

<!-- portfolio -->
<div class="abs centered script section-script" style="top:1466px">Photo Styles</div>
<h2 class="abs centered section-title caps" style="top:1534px">Our Portfolio</h2>
<div class="abs portfolio-panel"></div>
<div class="abs style-card" style="left:127px"><div class="frame" role="img" aria-label="Couple by a stone house, signature edit"></div><p>Colm's Hallmark</p></div>
<div class="abs style-card" style="left:368px"><div class="frame airy" role="img" aria-label="Couple by a stone house, bright and airy edit"></div><p>Bright &amp; Airy</p></div>
<div class="abs style-card" style="left:609px"><div class="frame oak" role="img" aria-label="Couple by a stone house, warm brown edit"></div><p>Silken Oak</p></div>
<div class="abs style-card" style="left:850px"><div class="frame mono" role="img" aria-label="Couple by a stone house, black and white edit"></div><p>Black &amp; White</p></div>
<div class="abs round-btn" style="left:47px;top:1825px"><svg width="16" height="16" viewBox="0 0 16 16"><path d="M10 3 5 8l5 5" fill="none" stroke="#333" stroke-width="1.8"/></svg></div>
<div class="abs round-btn" style="left:1101px;top:1825px"><svg width="16" height="16" viewBox="0 0 16 16"><path d="M6 3l5 5-5 5" fill="none" stroke="#333" stroke-width="1.8"/></svg></div>

<!-- testimonials -->
<div class="abs centered script section-script" style="top:2218px">Reviews</div>
<h2 class="abs centered section-title caps" style="top:2288px">Client Testimonials</h2>

<div class="abs review" style="left:112px;top:2517px;width:308px;height:370px;padding-top:70px">
  <q>“ Colm is the absolute best! He did a SPECTACULAR job with our wedding photos. He got images of everything, even the things that we never thought he would notice. Hands down Colm is the best photographer I have seen in the area and you will not be disappointed. ”</q>
  <div class="who">Dana &amp; Eli</div>
</div>
<div class="abs avatar" style="left:221px;top:2472px" role="img" aria-label="Couple portrait"></div>

<div class="abs review featured" style="left:446px;top:2430px;width:308px;height:370px;padding-top:60px">
  <q>“Colm did an outstanding job on our wedding photos! We got so so much more for so so much less. Thanks again Colm, you exceeded our expectations and then some. I recommend him 100 times over! ”</q>
  <div class="who" style="margin-top:70px">Sam &amp; Nora</div>
</div>
<div class="abs avatar blue" style="left:555px;top:2381px" role="img" aria-label="Couple portrait"></div>

<div class="abs review" style="left:780px;top:2517px;width:308px;height:370px;padding-top:70px">
  <q>“ Colm did a fabulous job on both our engagement and wedding photos. We were very impressed with not only the posed shots but also all off the candid ones. He was very professional, organized and accommodating. We have already recommended...</q>
  <div class="who">Ravi &amp; June</div>
</div>
<div class="abs avatar" style="left:889px;top:2472px" role="img" aria-label="Couple portrait"></div>

<div class="abs dots"><span></span><span class="on"></span><span></span><span></span><span></span><span></span></div>

<!-- contact -->
<div class="abs centered script section-script" style="top:3024px">Get in touch</div>
<h2 class="abs centered section-title caps" style="top:3096px">Contact Me</h2>
<div class="abs field" style="left:191px;top:3210px;width:403px;height:52px">Name</div>
<div class="abs field" style="left:615px;top:3210px;width:395px;height:52px">Email Address</div>
<div class="abs field" style="left:191px;top:3282px;width:819px;height:51px">Phone Number</div>
<div class="abs field" style="left:191px;top:3353px;width:819px;height:130px">Event Date/Info</div>
<div class="abs outline-btn" style="left:488px;top:3537px;width:222px;height:59px;font-weight:500">Check Availability</div>

<!-- footer -->
<footer class="abs site-footer">
  <div class="abs footer-brand"><span class="ring"></span>Colm V Photography</div>
  <p class="abs footer-text">Get in touch with me and we chat about your wedding, engagement, or other photos.</p>
  <div class="abs contact-line" style="top:148px">
    <svg width="16" height="12" viewBox="0 0 16 12"><rect width="16" height="12" rx="1" fill="var(--teal)"/><path d="M1 1l7 5 7-5" fill="none" stroke="var(--footer)" stroke-width="1.3"/></svg>
    Email: colm@colmvphotography.com
  </div>
  <div class="abs contact-line" style="top:182px">
    <svg width="14" height="14" viewBox="0 0 14 14"><path d="M3 1l2.5 3-1.5 1.5c.8 1.8 2.2 3.2 4 4L9.5 8l3 2.5-1.5 2.5C6 13 1 8 .5 2.5z" fill="var(--teal)"/></svg>
    Phone: 555-014-2281
  </div>
  <div class="abs social" style="left:981px;top:98px" aria-label="Social profile"></div>
  <div class="abs social" style="left:1041px;top:98px" aria-label="Social profile"></div>
  <p class="abs copyright">Copyright ©2025 Colm V Photography.</p>
</footer>

</body>
</html>
```